I need a business card design for a new company that will be doing consulting work around issues of cultural competency, and diversity and inclusion. I would like the design to be crisp and clear with bold but conservative colors and incorporate shades of blue

Target Market(s)

Small businesses, schools, non-profits

Industry/Entity Type

Consulting

Font styles to use
Serif
Sans Serif

Colors
0c5ba6
6b449b
3276b5
0292cd

Requirements
Must have
• A Morrow Venture (name of company)
• Lemlem Tavish
• CEO
• lemlem@amorrowventure.com
• (215)483-2756

```html
<!DOCTYPE html>
<html lang="en">
<head>
<meta charset="utf-8">
<title>A Morrow Venture — Business Card</title>
<link rel="stylesheet" href="https://fonts.googleapis.com/css2?family=Oswald:wght@500;600&family=Lato:wght@400;700&display=swap">
<style>
  :root {
    --card-white: #f5f5f3;
    --page-bg: #e6e6e4;
    --band-dark: #2a2b30;
    --panel-dark: #37383d;
    --info-dark: #34353a;
    --chevron-blue: #4a87c2;
    --tab-blue: #3a5fb3;
    --rule-blue: #2f57b0;
    --name-blue: #3f82cc;
    --text-light: #e4e4e6;
    --text-white: #ffffff;
  }
  html, body {
    margin: 0;
    padding: 0;
    width: 1200px;
    height: 789px;
    overflow: hidden;
    background: var(--page-bg);
  }
  .card {
    position: relative;
    width: 1200px;
    height: 789px;
    background: var(--card-white);
    overflow: hidden;
  }
  .card-graphics {
    position: absolute;
    inset: 0;
  }
  .brand {
    position: absolute;
    left: 90px;
    top: 318px;
    width: 300px;
    margin: 0;
    font-family: "Oswald", sans-serif;
    font-weight: 600;
    font-size: 54px;
    line-height: 1.08;
    letter-spacing: 1px;
    color: var(--text-white);
    text-transform: uppercase;
  }
  .brand span { display: block; }
  .person {
    position: absolute;
    left: 735px;
    top: 168px;
    margin: 0;
  }
  .person-name {
    margin: 0;
    font-family: "Oswald", sans-serif;
    font-weight: 600;
    font-size: 56px;
    line-height: 1;
    text-transform: uppercase;
    color: var(--text-white);
  }
  .person-name .surname { color: var(--name-blue); }
  .person-title {
    margin: 2px 0 0 4px;
    font-family: "Lato", sans-serif;
    font-weight: 700;
    font-size: 20px;
    letter-spacing: 7px;
    color: var(--text-white);
  }
  .contact {
    position: absolute;
    left: 735px;
    margin: 0;
    font-family: "Lato", sans-serif;
    font-weight: 400;
    color: var(--text-light);
  }
  .contact-phone { top: 318px; font-size: 30px; letter-spacing: 0.5px; }
  .contact-email { top: 448px; font-size: 28px; }
  .contact-address { top: 556px; font-size: 26px; line-height: 1.3; }
  .contact-address span { display: block; }
</style>
</head>
<body>
<main class="card">
  <svg class="card-graphics" width="1200" height="789" viewBox="0 0 1200 789" aria-hidden="true">
    <!-- contact band -->
    <rect class="contact-band" x="360" y="150" width="800" height="510" fill="var(--band-dark)"/>
    <!-- info panel -->
    <rect class="info-panel" x="690" y="150" width="470" height="510" fill="var(--info-dark)"/>
    <!-- white gap around chevron -->
    <polygon class="chevron-gap" points="330,150 497,150 568,405 497,660 330,660" fill="var(--card-white)"/>
    <!-- blue chevron -->
    <polygon class="chevron" points="363,150 483,150 554,405 483,660 363,660 434,405" fill="var(--chevron-blue)"/>
    <!-- brand panel -->
    <polygon class="brand-panel" points="70,80 330,80 420,405 330,730 70,730" fill="var(--panel-dark)"/>

    <!-- row rules -->
    <g class="row-rules" stroke="var(--rule-blue)" stroke-width="3">
      <line x1="530" y1="277" x2="1160" y2="277"/>
      <line x1="566" y1="405" x2="1160" y2="405"/>
      <line x1="530" y1="532" x2="1160" y2="532"/>
    </g>

    <!-- icon tabs -->
    <g class="icon-tabs" fill="var(--tab-blue)">
      <path d="M690 183 H638 a30 30 0 0 0 0 60 H690 Z"/>
      <path d="M690 311 H638 a30 30 0 0 0 0 60 H690 Z"/>
      <path d="M690 438 H638 a30 30 0 0 0 0 60 H690 Z"/>
      <path d="M690 566 H638 a30 30 0 0 0 0 60 H690 Z"/>
    </g>

    <!-- icons -->
    <g class="icons" fill="var(--band-dark)">
      <!-- person -->
      <circle cx="652" cy="205" r="9"/>
      <path d="M636 230 a16 13 0 0 1 32 0 Z"/>
      <!-- phone -->
      <path d="M644 326 l7 -3 l5 11 l-5 4 a22 22 0 0 0 9 10 l4 -5 l11 5 l-3 7 c-18 2 -32 -14 -28 -29 Z"/>
      <!-- globe -->
      <circle cx="654" cy="468" r="15" fill="none" stroke="var(--band-dark)" stroke-width="3"/>
      <ellipse cx="654" cy="468" rx="6" ry="15" fill="none" stroke="var(--band-dark)" stroke-width="2.5"/>
      <line x1="639" y1="468" x2="669" y2="468" stroke="var(--band-dark)" stroke-width="2.5"/>
      <!-- pin -->
      <path d="M654 578 a13 13 0 0 1 13 13 c0 10 -13 24 -13 24 c0 0 -13 -14 -13 -24 a13 13 0 0 1 13 -13 Z"/>
      <circle cx="654" cy="591" r="5" fill="var(--tab-blue)"/>
    </g>
  </svg>

  <h1 class="brand"><span>Morrow</span><span>Venture</span></h1>

  <div class="person">
    <h2 class="person-name">Lemlem <span class="surname">Tavish</span></h2>
    <p class="person-title">CEO</p>
  </div>

  <p class="contact contact-phone">(215)483-2756</p>
  <p class="contact contact-email">lemlem@amorrowventure.com</p>
  <p class="contact contact-address">
    <span>put your adresse 1 here</span>
    <span>put your adresse 2 here</span>
  </p>
</main>
</body>
</html>
```